Super elegant, crisp & clean Business card design required

We recently upgraded our branding - which is on our website - tavorelstudio.com

I would like a simple, yet elegant, clean business card design please.

The font of my logo is Cinzel - and because of the natural colour - it's best to have this on a black background.

I would like to have the back of the business card - with simply my logo.

PLEASE DO NOT SUBMIT A COMPLICATED / UNCLEAN DESIGN

Industry/Entity Type

Business

Contact Information for Business Card

Dalvik Ostrander Photography

Font styles to use
Other font styles liked:
• Cinzel

Requirements
Must have
• A backpage with nothing but my logo
• Simple design - stands out
Should not have
• Colour that dont align with my logo
• Over complicated '/ non symmetrical design

```html
<!DOCTYPE html>
<html lang="en">
<head>
<meta charset="utf-8">
<title>Dalvik Ostrander Photography – Business Card</title>
<link href="https://fonts.googleapis.com/css2?family=Cinzel:wght@400&family=Source+Sans+3:wght@400&display=swap" rel="stylesheet">
<style>
  :root {
    --backdrop: #3b3b3b;
    --card: #ffffff;
    --bronze: #7b6b57;
    --ink: #5d5247;
    --shadow: rgba(0, 0, 0, 0.55);
  }
  * { margin: 0; padding: 0; box-sizing: border-box; }
  html, body {
    width: 1200px;
    height: 1200px;
    overflow: hidden;
    background: var(--backdrop);
  }
  .stage {
    position: relative;
    width: 1200px;
    height: 1200px;
  }
  .card {
    position: absolute;
    left: 305px;
    width: 589px;
    height: 333px;
    background: var(--card);
    border-radius: 18px;
    box-shadow: 4px 6px 10px var(--shadow);
    overflow: hidden;
  }
  .card--front { top: 221px; }
  .card--back { top: 645px; }

  /* Front */
  .wordmark {
    position: absolute;
    left: 0;
    right: 0;
    top: 140px;
    text-align: center;
    color: var(--bronze);
  }
  .wordmark__name {
    font-family: "Cinzel", serif;
    font-size: 27px;
    letter-spacing: 0.5px;
    line-height: 1;
  }
  .wordmark__trade {
    font-family: "Cinzel", serif;
    font-size: 11px;
    letter-spacing: 6px;
    margin-top: 4px;
    padding-left: 6px;
  }

  /* Back */
  .back-mark {
    position: absolute;
    right: 46px;
    top: 86px;
    font-family: "Cinzel", serif;
    font-size: 14px;
    color: var(--bronze);
    letter-spacing: 0.5px;
  }
  .accent-bar {
    position: absolute;
    left: 0;
    top: 201px;
    width: 11px;
    height: 28px;
    background: var(--bronze);
  }
  .holder-name {
    position: absolute;
    left: 29px;
    top: 201px;
    font-family: "Cinzel", serif;
    font-size: 24px;
    line-height: 28px;
    color: var(--bronze);
  }
  .contact-list {
    position: absolute;
    left: 29px;
    top: 245px;
    list-style: none;
    font-family: "Source Sans 3", sans-serif;
    font-size: 16px;
    color: var(--ink);
  }
  .contact-list li {
    display: flex;
    align-items: center;
    height: 22.5px;
  }
  .contact-list svg {
    width: 12px;
    height: 12px;
    margin-right: 11px;
    flex: none;
  }
</style>
</head>
<body>
<main class="stage">
  <section class="card card--front" aria-label="Card front">
    <div class="wordmark">
      <div class="wordmark__name">Dalvik Ostrander</div>
      <div class="wordmark__trade">PHOTOGRAPHY</div>
    </div>
  </section>

  <section class="card card--back" aria-label="Card back">
    <div class="back-mark">Dalvik Ostrander</div>
    <div class="accent-bar"></div>
    <h1 class="holder-name">Dalvik Ostrander</h1>
    <ul class="contact-list">
      <li>
        <svg viewBox="0 0 12 12" aria-hidden="true"><path fill="var(--ink)" d="M1 3.5C1 2 3 1.5 6 1.5S11 2 11 3.5V5H8.5V4H3.5V5H1Z M2.5 6L4 4.5H8L9.5 6V10.5H2.5Z"/><circle cx="6" cy="7.6" r="1.3" fill="#fff"/></svg>
        000.0000
      </li>
      <li>
        <svg viewBox="0 0 12 12" aria-hidden="true"><rect x="0.5" y="2.5" width="11" height="7.5" fill="var(--ink)"/><path d="M0.8 2.8L6 7L11.2 2.8" stroke="#fff" stroke-width="1" fill="none"/></svg>
        contact@tavorelstudio.com
      </li>
      <li>
        <svg viewBox="0 0 12 12" aria-hidden="true"><g fill="none" stroke="var(--ink)" stroke-width="0.9"><circle cx="6" cy="6" r="5"/><ellipse cx="6" cy="6" rx="2.2" ry="5"/><path d="M1 6H11M2 3.3H10M2 8.7H10"/></g></svg>
        www.tavorelstudio.com
      </li>
    </ul>
  </section>
</main>
</body>
</html>
```